Flyer für Mobile Massage am Arbeitsplatz
Zielgruppe
Der Flyer richtet sich an Geschäftsleitungen, Firmenvorstände, Betriebsräte.
Ich werde den Flyer sowohl persönlich überreichen, als auch postalisch verschicken.
Aufgabenstellung
Es geht um einen Flyer, DIN lang, Hochformat, beidseitig bedruckt.

```html
<!DOCTYPE html>
<html lang="de">
<head>
<meta charset="utf-8">
<title>Mobile Massage am Arbeitsplatz – Flyer DIN lang</title>
<link href="https://fonts.googleapis.com/css2?family=Arimo:wght@400;700&display=swap" rel="stylesheet">
<style>
  :root {
    --stage: #e9e6e1;
    --paper: #ffffff;
    --swoosh: #eeeeee;
    --swoosh-dark: #dcdcdc;
    --green: #3f8a1f;
    --green-light: #7fbf4f;
    --frame: #b9dca0;
    --text: #333333;
    --muted: #666666;
    --footer: #d9d9d9;
    --photo-a: #b9a58e;
    --photo-b: #7d8a78;
  }
  * { box-sizing: border-box; margin: 0; padding: 0; }
  html, body { width: 1200px; height: 899px; overflow: hidden; }
  body {
    background: var(--stage);
    font-family: "Arimo", Arial, sans-serif;
    color: var(--text);
    position: relative;
  }
  .flyer-page {
    position: absolute;
    top: 34px;
    width: 400px;
    height: 830px;
    background: var(--paper);
    overflow: hidden;
    box-shadow: 0 2px 10px rgba(0,0,0,.18);
  }
  .flyer-page--front { left: 170px; }
  .flyer-page--back { left: 630px; }
  .swoosh { position: absolute; inset: 0; width: 100%; height: 100%; }
  .photo {
    position: absolute;
    border: 3px solid var(--frame);
    background: linear-gradient(135deg, var(--photo-a), var(--photo-b));
  }
  .headline {
    position: absolute;
    top: 58px; left: 90px;
    color: var(--green);
    font-weight: 700;
    font-size: 34px;
    letter-spacing: .2px;
  }
  .subline {
    position: absolute;
    top: 104px; left: 98px;
    color: var(--green);
    font-size: 17px;
  }
  .phone {
    position: absolute;
    top: 722px; left: 34px;
    color: var(--green);
    font-size: 20px;
  }
  .footer {
    position: absolute;
    left: 0; right: 0; bottom: 0;
    height: 40px;
    background: var(--footer);
    color: var(--muted);
    font-size: 12px;
    text-align: center;
    line-height: 40px;
  }
  .copy {
    position: absolute;
    top: 205px; left: 36px; right: 30px;
    text-align: center;
    font-size: 13px;
    line-height: 17px;
  }
  .copy p { margin-bottom: 13px; }
  .copy .accent { color: var(--green); }
  .prices { margin-top: 4px; }
  .prices .label { color: var(--green); }
</style>
</head>
<body>

<section class="flyer-page flyer-page--front">
  <svg class="swoosh" viewBox="0 0 400 830" aria-hidden="true">
    <path d="M0 120 C120 60 260 40 400 90 L400 0 L0 0 Z" fill="var(--swoosh)"/>
    <path d="M0 520 C140 460 280 600 400 560 L400 830 L0 830 Z" fill="var(--swoosh)"/>
    <path d="M0 560 C150 500 280 640 400 600" fill="none" stroke="var(--swoosh-dark)" stroke-width="2"/>
  </svg>
  <h1 class="headline">Mobile Massage</h1>
  <p class="subline">am Arbeitsplatz</p>

  <div class="photo" style="left:28px;top:170px;width:190px;height:250px" role="img" aria-label="Foto: Masseur neben einem Massagestuhl im Büro"></div>
  <div class="photo" style="left:240px;top:150px;width:135px;height:120px" role="img" aria-label="Foto: Massage auf dem Massagestuhl"></div>
  <div class="photo" style="left:240px;top:290px;width:135px;height:125px" role="img" aria-label="Foto: Nackenmassage am Arbeitsplatz"></div>
  <div class="photo" style="left:240px;top:435px;width:135px;height:120px" role="img" aria-label="Foto: Schultermassage auf dem Massagestuhl"></div>
  <div class="photo" style="left:40px;top:470px;width:95px;height:170px" role="img" aria-label="Foto: Rückenmassage im Büro"></div>
  <div class="photo" style="left:150px;top:575px;width:130px;height:110px" role="img" aria-label="Foto: Armmassage auf dem Massagestuhl"></div>

  <p class="phone">Tel.: 030-48120937</p>
  <p class="footer">www.massage-vor-ort-havelland.de</p>
</section>

<section class="flyer-page flyer-page--back">
  <svg class="swoosh" viewBox="0 0 400 830" aria-hidden="true">
    <path d="M0 60 C130 20 270 10 400 40 L400 0 L0 0 Z" fill="var(--swoosh)"/>
    <path d="M0 620 C140 580 280 680 400 640 L400 830 L0 830 Z" fill="var(--swoosh)"/>
    <path d="M0 650 C150 610 280 710 400 670" fill="none" stroke="var(--swoosh-dark)" stroke-width="2"/>
  </svg>

  <div class="photo" style="left:30px;top:30px;width:150px;height:130px" role="img" aria-label="Foto: Massage auf dem Massagestuhl"></div>
  <div class="photo" style="left:220px;top:40px;width:150px;height:130px" role="img" aria-label="Foto: Schulterlockerung im Büro"></div>

  <div class="copy">
    <p>In unseren Massagen am Arbeitsplatz lassen wir Elemente aus der <span class="accent">Shiatsu - Energiemassage</span> und dem <span class="accent">Joint Release - Gelenklockerungen</span> zusammenfließen.</p>
    <p>Auf diese Weise eröffnen wir einen Raum für spürbare <span class="accent">Entspannung mitten im Arbeitsalltag</span>.</p>
    <p>Die Massagen befreien aus berufsbedingten Zwangshaltungen, wirken stresslindernd und stimmungshebend im Team, fokussieren auf die Problemzonen im Büro: Rücken, Nacken, Schulter und Mausarm und sind ein Baustein im innerbetrieblichen Gesundheitsmanagement.</p>
    <p>Die Kosten können, sofern vom Arbeitgeber getragen, nach §3 Nr. 34 EStG von der Steuer abgesetzt werden.</p>
    <p class="prices"><span class="label">Preis:</span><br>20 Minuten : 16 Euro<br>inklusive Anfahrt<br>buchbar ab 4 Personen</p>
  </div>

  <div class="photo" style="left:22px;top:655px;width:110px;height:120px" role="img" aria-label="Foto: Nackenmassage am Schreibtisch"></div>
  <div class="photo" style="left:145px;top:665px;width:110px;height:110px" role="img" aria-label="Foto: Rückenmassage auf dem Massagestuhl"></div>
  <div class="photo" style="left:268px;top:650px;width:110px;height:125px" role="img" aria-label="Foto: Armmassage im Büro"></div>

  <p class="footer">www.massage-vor-ort-havelland.de</p>
</section>

</body>
</html>
```